Leave Behind Flyer Project for Print

Project Goal: Create a leave-behind flyer promoting Skyrun Motion to our customers: Multihousing property managers, hospitality, boutique gyms, high schools, colleges & resellers.

Theme: entry-level commercial products for a value price

Theme Heading: COMMERCIAL – GRADE GYM EQUIPMENT THAT WON’T BREAK THE BANK

Description: Skyrun Motion Cardio Equipment is a boutique brand of incredibly affordable, commercial fitness equipment. Save thousands by letting Skyrun Motion be your turnkey solution for cardio fitness equipment. Search now for a low-price guarantee, quality fitness equipment with excellent customer service.

Company Promoting it: Coral Vigor Partners

Company Address: 4817 Heron Way, Fort Myers, FL 33358 | Phone : (239) 555-0174

Email: Sales@CoralVigorPartners.example website: CoralVigorPartners.example
Company Logo:

Products Being Promoted: Skyrun Motion – links to photos and descriptions below:
K4 Treadmill
https://skyrunmotion.example/product/k4/
P3 Elliptical
https://skyrunmotion.example/product/p3/
T2 Upright Bike
https://skyrunmotion.example/product/t2/
V9 Recumbent Bike
https://skyrunmotion.example/product/v9/

Flyer size: 8.5” x 11,” Vertical, Full Color, Front / Back

InDesign Template: https://files.presslumo.example/templates/presslumo.example/flyer-8.5inx11in-v.indd.zip

Photoshop Template: https://files.presslumo.example/templates/presslumo.example/flyer-8.5inx11in-v.psd.zip

Illustrator: https://files.presslumo.example/templates/presslumo.example/flyer-8.5inx11in-v.ai.zip

Target Market(s)

Multihousing property managers, hospitality, boutique gyms, high schools, colleges & resellers.

Industry/Entity Type

Fitness equipment

Requirements
Must have
• Equipment pictures, equipmet model numbers, description
Nice to have
• Modern Flyer

```html
<!DOCTYPE html>
<html lang="en">
<head>
<meta charset="utf-8">
<title>Skyrun Motion Flyer – Coral Vigor Partners</title>
<link rel="stylesheet" href="https://fonts.googleapis.com/css2?family=Bebas+Neue&family=Poppins:ital,wght@0,400;0,500;0,600;0,700;0,800;1,600;1,800&display=swap">
<style>
:root{
  --navy:#0d2656;
  --navy-deep:#081b40;
  --gold:#e9ac1c;
  --white:#ffffff;
  --ink:#1b1b1b;
  --stage:#e2e2e2;
}
*{box-sizing:border-box;margin:0;padding:0}
html,body{width:1200px;height:1200px;overflow:hidden;background:var(--stage);font-family:'Poppins',sans-serif}
.page{position:absolute;top:209px;width:535px;height:690px;background:var(--white);overflow:hidden}
.page--front{left:43px}
.page--back{left:615px}
.layer{position:absolute;left:0;top:0}
.abs{position:absolute}

/* front */
.accent-rule{left:38px;top:0;width:3px;height:263px;background:var(--gold)}
.kicker{left:63px;top:36px;color:var(--white);font-weight:400;font-size:27px;letter-spacing:7px;line-height:1}
.grade{left:63px;top:74px;color:var(--white);font-weight:800;font-style:italic;font-size:39px;line-height:1;letter-spacing:1px}
.gym{left:58px;top:112px;color:var(--gold);font-family:'Bebas Neue',sans-serif;font-size:208px;line-height:.8;letter-spacing:1px;transform:scaleX(.98);transform-origin:left top}
.equipment{left:34px;top:272px;color:var(--gold);font-family:'Bebas Neue',sans-serif;font-size:66px;line-height:.85;letter-spacing:.5px}
.tagline{left:34px;top:333px;color:var(--white);font-size:19px;line-height:23px;letter-spacing:3.2px;font-weight:400}
.intro{left:35px;top:398px;width:200px;color:var(--white);font-size:9.6px;line-height:11.35px;font-weight:500}

.brand{display:flex;align-items:center;gap:6px;white-space:nowrap}
.brand-dot{width:14px;height:14px;border-radius:50%;background:var(--gold);flex:none}
.brand-name{color:var(--navy);font-weight:600;letter-spacing:-.2px}
.brand--front{left:35px;top:580px}
.brand--front .brand-name{font-size:20px}
.brand--back{left:352px;top:44px}
.brand--back .brand-name{font-size:13.5px}

.contact{display:flex;align-items:center;gap:6px;color:var(--ink);white-space:nowrap}
.contact svg{flex:none}
.phone-front{left:274px;top:571px;font-size:17px;font-weight:600}
.addr-front{left:276px;top:598px;font-size:11.5px;font-weight:500}

.pill{height:24px;border:2.5px solid var(--gold);border-radius:12px;overflow:hidden;display:flex;background:var(--gold)}
.pill-mail{background:var(--white);border-radius:12px;display:flex;align-items:center;justify-content:center;font-size:10.5px;color:var(--ink);font-weight:400}
.pill-web{flex:1;display:flex;align-items:center;justify-content:center;font-size:12.5px;font-weight:800;color:var(--navy);letter-spacing:.6px}
.pill--front{left:33px;top:629px;width:472px}
.pill--back{left:33px;top:629px;width:472px}
.pill-mail{width:236px}

/* back */
.section-title{left:147px;top:40px;font-size:20px;font-weight:800;font-style:italic;color:var(--navy-deep);letter-spacing:.3px}
.section-title span{color:var(--gold)}
.product-shot{position:absolute;left:32px;width:106px;height:106px;border-radius:50%;border:3px solid var(--gold);background:radial-gradient(circle at 50% 50%,#ffffff 0%,#f1f2f4 70%,#dcdfe4 100%);overflow:hidden}
.product{position:absolute;left:150px;width:359px}
.product h2{font-size:12px;font-weight:700;color:var(--navy-deep);line-height:1;margin-bottom:6px;letter-spacing:.1px}
.product p{font-size:6.7px;line-height:8.2px;color:var(--ink);text-align:justify;margin-bottom:5px}
.phone-back{left:106px;top:595px;font-size:18px;font-weight:600}
.addr-back{left:267px;top:598px;font-size:11.5px;font-weight:500}
</style>
</head>
<body>

<!-- FRONT -->
<section class="page page--front">
  <svg class="layer" width="535" height="690" viewBox="0 0 535 690">
    <defs>
      <linearGradient id="runPhoto" x1="0" y1="0" x2="0.4" y2="1">
        <stop offset="0" stop-color="#123a8a"/>
        <stop offset="0.45" stop-color="#1d47a0"/>
        <stop offset="0.7" stop-color="#8d9aac"/>
        <stop offset="1" stop-color="#d5dbe3"/>
      </linearGradient>
    </defs>
    <rect width="535" height="560" fill="var(--navy)"/>
    <g role="img" aria-label="Photo of a runner in blue leggings and sneakers on a treadmill belt">
      <polygon points="338,0 535,0 535,560 210,560 262,300 300,150" fill="url(#runPhoto)"/>
    </g>
    <path d="M0,545 L18,542 L34,547 L52,541 L70,546 L92,540 L110,545 L130,541 L150,546 L172,540 L196,545 L220,541 L246,546 L270,541 L296,545 L322,540 L350,546 L378,541 L404,545 L432,540 L460,546 L488,541 L512,545 L535,540 L535,690 L0,690 Z" fill="var(--white)"/>
  </svg>

  <div class="abs accent-rule"></div>
  <div class="abs kicker">COMMERCIAL</div>
  <div class="abs grade">GRADE</div>
  <div class="abs gym">GYM</div>
  <div class="abs equipment">EQUIPMENT</div>
  <div class="abs tagline">THAT WON’T<br>BREAK THE BANK</div>
  <p class="abs intro">Skyrun Motion Cardio Equipment is a boutique brand of incredibly affordable, commercial fitness equipment. Save thousands by letting Skyrun Motion be your turnkey solution for cardio fitness equipment. Search now for a low-price guarantee, quality fitness equipment with excellent customer service.</p>

  <div class="abs brand brand--front"><span class="brand-dot"></span><span class="brand-name">Coral Vigor Partners</span></div>

  <div class="abs contact phone-front">
    <svg width="15" height="15" viewBox="0 0 24 24"><path d="M6.6 10.8a15.1 15.1 0 0 0 6.6 6.6l2.2-2.2c.3-.3.7-.4 1-.2 1.1.4 2.3.6 3.6.6.6 0 1 .4 1 1V20c0 .6-.4 1-1 1A17 17 0 0 1 3 4c0-.6.4-1 1-1h3.5c.6 0 1 .4 1 1 0 1.3.2 2.5.6 3.6.1.3 0 .7-.2 1z" fill="#1d4fb0"/></svg>
    <span>(239) 555-0174</span>
  </div>
  <div class="abs contact addr-front">
    <svg width="12" height="16" viewBox="0 0 24 32"><path d="M12 0a12 12 0 0 0-12 12c0 9 12 20 12 20s12-11 12-20A12 12 0 0 0 12 0zm0 17a5 5 0 1 1 0-10 5 5 0 0 1 0 10z" fill="#1d4fb0"/></svg>
    <span>4817 Heron Way, Fort Myers, FL 33358</span>
  </div>

  <div class="abs pill pill--front">
    <span class="pill-mail">Sales@CoralVigorPartners.example</span>
    <span class="pill-web">CoralVigorPartners.example</span>
  </div>
</section>

<!-- BACK -->
<section class="page page--back">
  <svg class="layer" width="535" height="690" viewBox="0 0 535 690" role="img" aria-label="Dark blue photo strip of a person training at the gym">
    <path d="M0,0 L90,0 L88,20 L93,48 L86,80 L92,120 L84,170 L90,220 L86,260 L93,300 L85,350 L91,400 L84,450 L90,500 L86,550 L92,600 L87,650 L91,690 L0,690 Z" fill="var(--navy)"/>
  </svg>

  <h1 class="abs section-title">OUR <span>PRODUCTS</span></h1>
  <div class="abs brand brand--back"><span class="brand-dot"></span><span class="brand-name">Coral Vigor Partners</span></div>

  <div class="product-shot" style="top:76px" role="img" aria-label="K4 treadmill product photo"></div>
  <div class="product-shot" style="top:202px" role="img" aria-label="P3 elliptical product photo"></div>
  <div class="product-shot" style="top:337px" role="img" aria-label="T2 upright bike product photo"></div>
  <div class="product-shot" style="top:457px" role="img" aria-label="V9 recumbent bike product photo"></div>

  <article class="product" style="top:82px">
    <h2>K4 (AC/DC) TREADMILL</h2>
    <p>With its powerful motor and durable frame, the K4 Treadmill is the perfect choice for fitness enthusiasts. This treadmill offers a great deal of versatility with its highlighted features – a high-efficiency 4.25 HP DC motor OR 3.5 HP AC motor, a 60”x20” lubricant-infused, thermoplastic polyurethane (TPU) running belt, and a shock-absorbing, maintenance-free deck. The K4 also offers additional comfort features, such as contact and telemetric heart-rate sensors, a cooling fan, speakers, and USB charging port. Perfectly designed for maximum performance and portability, the K4’s small footprint and easy-to-move front-mounted dual wheels make it easy to move from spot to spot. With its full commercial components on a durable light-commercial frame and zinc-dipped anti-corrosion coating for superior rust protection, the K4 Treadmill is a reliable and tough machine that is perfect for any commercial facility!</p>
  </article>

  <article class="product" style="top:203px">
    <h2>P3 ELLIPTICAL</h2>
    <p>The P3 Elliptical is the perfect solution to your fitness routine. This light commercial elliptical offers an ergonomic design, low step-up height, and a 20” natural stride, all perfect for everyday use.</p>
    <p>The environmentally friendly machine is a self-powered cordless model and is designed to last; features include a zinc-dipped anti-corrosion coating for superior rust protection, along with a durable light-commercial frame and full-commercial components.</p>
    <p>The intuitive touchpad offers you control over your workout with a quick resistance shifter – no need to get off the machine to adjust. You can keep track of your performance and heart rate with the contact and telemetric heart-rate sensors and read while working out with the convenient reading rack/tablet holder.</p>
  </article>

  <article class="product" style="top:349px">
    <h2>T2 UPRIGHT BIKE</h2>
    <p>The T2 Upright Bike is built with fitness enthusiasts in mind. Our light commercial grade construction offers a powerful blend of convenience and durability. With the unique, self-powered cordless design, large ergonomic pedals with adjustable straps, and an easy-pull adjustable seat – your riding experience will be smooth, secure, and comfortable. Looking for an extra challenge? Factor in the triathlon-style handlebars and 13 levels of resistance for a rigorous hill-climbing workout. Enjoy additional convenience with our secure tablet holder and reading rack. Plus, our zinc-dipped anti-corrosion coating and small footprint for easy storage ensure the T2 Upright Bike will be a reliable workout partner for years to come. Get your new ride today!</p>
  </article>

  <article class="product" style="top:469px">
    <h2>V9 RECUMBENT BIKE</h2>
    <p>The V9 Recumbent Bike is the perfect combination of convenience and comfort for the fitness enthusiast looking for a premium, light commercial experience! This bike features an ergonomic and adjustable design, convenient oversized pedals, adjustable straps, and a walk-through frame design. With an easy-glide, 13-level adjustable seat and contact and telemetric heart-rate sensors, you’ll have access to various settings to maximize your workout. The integrated reading rack and tablet holder allow you to access entertainment while exercising easily, and an anti-corrosion zinc-dipped coating ensures superior rust protection. All these features are contained within a full commercial-grade frame that occupies only a small footprint, making the V9 Recumbent Bike a must-have for any fitness enthusiast looking for the most out of their exercise routine.</p>
  </article>

  <div class="abs contact phone-back">
    <svg width="16" height="16" viewBox="0 0 24 24"><path d="M6.6 10.8a15.1 15.1 0 0 0 6.6 6.6l2.2-2.2c.3-.3.7-.4 1-.2 1.1.4 2.3.6 3.6.6.6 0 1 .4 1 1V20c0 .6-.4 1-1 1A17 17 0 0 1 3 4c0-.6.4-1 1-1h3.5c.6 0 1 .4 1 1 0 1.3.2 2.5.6 3.6.1.3 0 .7-.2 1z" fill="var(--gold)"/></svg>
    <span>(239) 555-0174</span>
  </div>
  <div class="abs contact addr-back">
    <svg width="12" height="16" viewBox="0 0 24 32"><path d="M12 0a12 12 0 0 0-12 12c0 9 12 20 12 20s12-11 12-20A12 12 0 0 0 12 0zm0 17a5 5 0 1 1 0-10 5 5 0 0 1 0 10z" fill="var(--gold)"/></svg>
    <span>4817 Heron Way, Fort Myers, FL 33358</span>
  </div>

  <div class="abs pill pill--back">
    <span class="pill-mail">Sales@CoralVigorPartners.example</span>
    <span class="pill-web">CoralVigorPartners.example</span>
  </div>
</section>

</body>
</html>
```